Mobile App UI for Telecommunications/Hosting Company

We are about to convert our existing self-service Customer Portal into a mobile phone application and need an elegant and professional UI/UX design. Our company provides telecommunication (voice/mobile/data) and hosting services to medium-sized business. The primary purpose of the application is to view trouble tickets, alerts, orders, and performance charts. This application is available to customers only - not the general public.

Please provide a UI design suitable for display on iPhone/Android devices. The attached document includes a proposed screen flow. You are free to design your own screens to display the same information elegantly.
Updates

Please note that the design should be based on the wireframes in the Word document, not the screenshots.  The screenshots are just to show our existing web portal look & feel.

Also, just a few screens are required for initial submission (3 would be great).

Thanks,
Dermot.

Target Market(s)

IT Managers away from their desk and using a mobile phone application.
Adult males from technical background aged 30-50.
Customers of Brindlewood Networks have access to this application (not the general public). This is a self-service portal for customers only.

Industry/Entity Type

Business

Colors
0592cd
33a6d7
85cae6
cadf82
fde08a

Requirements
Must have
• Please look at the screenshots from our current Customer Portal site (part of the project brief). The mobile app does not have to look the same, but should follow a similar style.

Please check out our company web site at www.brindlewoodnetworks.example (this site is not the customer portal and has a different look at feel) to understand what Brindlewood Networks does.
Nice to have
• Sharing capabilities via email/SMS.
A nice background image to make it stand out
The colours selected below are a guide only as they are similar to the corporate colours
- The priority is something that works on a phone - a design extendable to tablets is a nice to have as our existing web site looks OK on a tablet..

```html
<!DOCTYPE html>
<html lang="en">
<head>
<meta charset="utf-8">
<title>Brindleview – Ticket Details</title>
<link href="https://fonts.googleapis.com/css2?family=Open+Sans:wght@400;600;700&display=swap" rel="stylesheet">
<style>
:root{
  --bg:#b4c5d4;
  --blue:#0592cd;
  --blue-mid:#33a6d7;
  --blue-light:#85cae6;
  --green:#cadf82;
  --yellow:#fde08a;
  --navy:#2c3b47;
  --navy-dark:#24323d;
  --paper:#ffffff;
  --mist:#e9eef2;
  --ink:#1e2a33;
  --line:#7fb9d8;
}
*{box-sizing:border-box;margin:0;padding:0}
html,body{width:1200px;height:1107px;overflow:hidden;background:var(--bg)}
body{font-family:"Open Sans",Arial,sans-serif;color:var(--ink);display:flex;align-items:center;justify-content:center}
.screen{width:560px;height:994px;background:var(--mist);display:flex;flex-direction:column;position:relative;overflow:hidden;box-shadow:0 10px 40px rgba(40,60,80,.25)}
.status-bar{height:35px;flex:none;background:var(--paper);display:flex;align-items:center;justify-content:space-between;padding:0 14px;font-size:14px;color:var(--blue)}
.status-bar .carrier{display:flex;align-items:center;gap:6px}
.status-bar .icons{display:flex;gap:8px;align-items:center}
.app-header{height:60px;flex:none;background:var(--paper);display:flex;align-items:center;position:relative}
.back{position:absolute;left:14px;display:flex;align-items:center;gap:6px;color:var(--blue);font-weight:700;font-size:15px}
.brand{margin:0 auto;display:flex;align-items:center;gap:8px;font-size:24px;font-weight:600;color:var(--navy)}
.brand .dot{width:20px;height:20px;border-radius:50%;background:var(--blue)}
.title-bar{height:40px;flex:none;background:var(--blue-light);display:flex;align-items:center;justify-content:center;gap:10px;color:var(--navy);font-weight:700;font-size:16px;letter-spacing:.5px}
.tabs{height:52px;flex:none;display:flex}
.tab{flex:1;display:flex;align-items:center;justify-content:center;color:#fff;font-size:16px;letter-spacing:.6px;background:var(--blue-mid);border-right:1px solid rgba(255,255,255,.35)}
.tab.active{background:var(--blue)}
.notify-band{height:70px;flex:none;background:var(--navy);display:flex;align-items:center;padding:0 18px;gap:14px}
.toggle{width:72px;height:34px;border-radius:17px;background:#6b7680;position:relative}
.toggle .knob{position:absolute;right:2px;top:2px;width:30px;height:30px;border-radius:50%;background:var(--green);display:flex;align-items:center;justify-content:center}
.notify-label{color:var(--green);font-size:14px;line-height:1.15;letter-spacing:.4px}
.contact-btn{margin-left:auto;background:var(--blue-mid);color:#fff;font-size:13px;padding:9px 22px}
.accent-line{height:4px;flex:none;background:var(--green)}
.ticket{height:150px;flex:none;background:var(--paper);display:flex;border-bottom:1px solid var(--line)}
.ticket-info{flex:1;padding:16px 18px;font-size:16px;line-height:1.5}
.ticket-info h1{font-size:16px;font-weight:600;margin-bottom:8px}
.actions{display:flex;flex-direction:column;width:150px}
.action{flex:1;display:flex;align-items:center;justify-content:center}
.action.call{background:var(--blue)}
.action.mail{border-left:1px solid var(--line);border-top:1px solid var(--line)}
.service{height:120px;flex:none;padding:16px 18px;font-size:16px;line-height:1.35;position:relative}
.service b{font-weight:700}
.reach{position:absolute;right:18px;top:16px;font-weight:700;display:flex;align-items:center;gap:8px}
.chev{width:24px;height:24px;border:2px solid var(--blue);border-radius:50%;display:inline-flex;align-items:center;justify-content:center;color:var(--blue);font-size:13px;font-weight:700}
.block{padding:10px 18px;position:relative;flex:none}
.tag{display:inline-block;font-size:14px;padding:4px 14px;letter-spacing:.4px;margin-bottom:6px}
.tag.alert{background:var(--green)}
.tag.resolution{background:var(--yellow)}
.block p{font-size:16px;display:flex;align-items:center;gap:10px}
.add-note{position:absolute;right:0;top:-30px;width:120px;height:110px;background:var(--blue);color:#fff;display:flex;flex-direction:column;align-items:center;justify-content:center;font-size:16px;line-height:1}
.notes-card{margin:12px 18px;background:var(--paper);padding:16px 18px;font-size:14px;line-height:1.4;border-radius:4px;box-shadow:0 1px 3px rgba(0,0,0,.08);flex:none}
.notes-card h2{color:var(--blue);font-size:18px;font-weight:700;margin-bottom:4px}
.notes-card time{font-weight:700;font-size:16px;margin-right:6px}
.tab-bar{margin-top:auto;height:80px;flex:none;background:var(--navy-dark);display:flex}
.tab-bar a{flex:1;display:flex;align-items:center;justify-content:center;color:var(--blue-mid);text-decoration:none;font-size:17px;letter-spacing:.6px;position:relative}
.tab-bar a.active{background:var(--blue);color:#fff}
.tab-bar a.active::before{content:"";position:absolute;top:-10px;left:50%;margin-left:-12px;border:12px solid transparent;border-top:0;border-bottom:10px solid var(--blue)}
</style>
</head>
<body>
<main class="screen">
  <div class="status-bar">
    <span class="carrier">
      <svg width="24" height="12"><rect x="0" y="8" width="3" height="4" fill="#0592cd"/><rect x="5" y="6" width="3" height="6" fill="#0592cd"/><rect x="10" y="4" width="3" height="8" fill="#0592cd"/><rect x="15" y="2" width="3" height="10" fill="#0592cd"/><rect x="20" y="0" width="3" height="12" fill="#0592cd"/></svg>
      CARRIER
    </span>
    <span>4:22 PM</span>
    <span class="icons">
      <svg width="14" height="14"><circle cx="7" cy="7" r="6" fill="#0592cd"/></svg>
      <svg width="14" height="14"><path d="M1 7 L13 1 L8 13 L7 8 Z" fill="#0592cd"/></svg>
      <svg width="30" height="14"><rect x="1" y="1" width="25" height="12" rx="2" fill="none" stroke="#0592cd" stroke-width="1.5"/><rect x="3" y="3" width="21" height="8" fill="#0592cd"/><rect x="27" y="5" width="2" height="4" fill="#0592cd"/></svg>
    </span>
  </div>

  <header class="app-header">
    <span class="back">
      <svg width="14" height="22"><path d="M12 2 L3 11 L12 20" stroke="#0592cd" stroke-width="3" fill="none"/></svg>
      BACK
    </span>
    <div class="brand"><span class="dot"></span>brindleview</div>
  </header>

  <div class="title-bar">
    <svg width="20" height="22"><rect x="2" y="2" width="16" height="18" fill="none" stroke="#2c3b47" stroke-width="2"/><path d="M6 8h8M6 12h8M6 16h5" stroke="#2c3b47" stroke-width="2"/></svg>
    TICKET DETAILS
  </div>

  <nav class="tabs">
    <span class="tab active">SUMMARY</span>
    <span class="tab">NOTES</span>
    <span class="tab">ATACHMENTS</span>
  </nav>

  <section class="notify-band">
    <div class="toggle"><span class="knob"><svg width="16" height="14"><path d="M2 7 L6 11 L14 2" stroke="#2c3b47" stroke-width="2" fill="none"/></svg></span></div>
    <div class="notify-label">NOTIFICATIONS<br>ENABLED</div>
    <span class="contact-btn">Contact us</span>
  </section>
  <div class="accent-line"></div>

  <section class="ticket">
    <div class="ticket-info">
      <h1>689277 – TRFX not showing in Sydney DSL service</h1>
      <div><b>Status:</b> Approved</div>
      <div><b>Date Logged:</b> Monday Jan1 2014 10:42 AM</div>
    </div>
    <div class="actions">
      <div class="action call">
        <svg width="52" height="52"><circle cx="26" cy="26" r="23" fill="none" stroke="#fff" stroke-width="2.5"/><path d="M17 16c2-2 4-1 5 1l2 4c1 2-1 3-2 4 1 3 4 6 7 7 1-1 2-3 4-2l4 2c2 1 3 3 1 5-3 3-8 2-14-4s-9-13-7-17z" fill="none" stroke="#fff" stroke-width="2.3"/></svg>
      </div>
      <div class="action mail">
        <svg width="52" height="52"><circle cx="26" cy="26" r="23" fill="none" stroke="#0592cd" stroke-width="2.5"/><rect x="13" y="17" width="26" height="18" fill="none" stroke="#0592cd" stroke-width="2.3"/><path d="M13 17 L26 28 L39 17" fill="none" stroke="#0592cd" stroke-width="2.3"/></svg>
      </div>
    </div>
  </section>

  <section class="service">
    <div><b>MDSL234567890</b> – Sydney DSL</div>
    <div>1Mbps/256Kbps</div>
    <div>Sydney Office</div>
    <span class="reach">Reached 99% <span class="chev">&gt;</span></span>
  </section>

  <section class="block">
    <span class="tag alert">LINKVIEW ALERTS</span>
    <p>Sydney IP Port (MPIPN123456790) <span class="chev">&gt;</span></p>
    <div class="add-note">
      <svg width="38" height="34"><rect x="3" y="6" width="24" height="24" fill="none" stroke="#fff" stroke-width="2.5"/><path d="M14 24 L15 14 M17 9 L17.5 9" stroke="#fff" stroke-width="3"/><path d="M24 12 L34 2" stroke="#fff" stroke-width="3"/></svg>
      <span style="margin-top:6px">Add</span><span>note</span>
    </div>
  </section>

  <section class="block">
    <span class="tag resolution">RESOLUTION COMMENT</span>
    <p>Filler text sample, filler text sample... <span class="chev">&gt;</span></p>
  </section>

  <article class="notes-card">
    <h2>Recent notes</h2>
    <p><time>7/2 11:00</time>This is not a fault as TRFX is not supposed on Corvane R40 routers for DSL services. Only Linkview standard is supported, which provides basic graphs and alerting capabilities...</p>
  </article>

  <nav class="tab-bar">
    <a class="active" href="#">TICKETS</a>
    <a href="#">ALERTS</a>
    <a href="#">ORDERS</a>
    <a href="#">SERVICES</a>
  </nav>
</main>
</body>
</html>
```